1/2 Page add for MERLT Conference

We are looking for a 1/2 page ad to support the annual MERLT conference. I want to encourage the attendees to come to our both so we can explain how they can save money on food and supplies. here is a link to the conference. https://www.merlt-example.org/conference/ here is our website www.pantryhubdirect-example.com - the what we do can be captured in the ad. We will be at booth 505. Our goal is to get people to our booth #505 to explain the services that we provide –

Discounted food pricing
Free menu planning/design
Use of Registered Dietitian
Huge selection of discounted PPE and other necessary supplies to run any child care center

We have over 6000 members in 46 States and work with both small and large food distributors. We have been a sponsor of the association for the last 10 years.

Target Market(s)

Child care centers

Requirements
Must have
• Booth number -outline of what we do --- Stress we are a FREE service getting our members reduced pricing on food and supplies

```html
<!DOCTYPE html>
<html lang="en">
<head>
<meta charset="utf-8">
<title>Pantry Hub Direct – Booth 505</title>
<link rel="stylesheet" href="https://fonts.googleapis.com/css2?family=Roboto:wght@300;400;700&family=Work+Sans:wght@400;600&family=Open+Sans:wght@400;600&display=swap">
<style>
  :root {
    --green: #8ff56b;
    --green-pale: #c9f9b6;
    --blue: #4aa3ff;
    --blue-text: #4a9df2;
    --ink: #111111;
    --grey: #5f6368;
    --white: #ffffff;
    --paper: #ffffff;
  }
  * { margin: 0; padding: 0; box-sizing: border-box; }
  html, body { width: 1200px; height: 800px; overflow: hidden; background: var(--paper); }
  .ad {
    position: relative;
    width: 1200px;
    height: 800px;
    overflow: hidden;
    background: var(--paper);
    font-family: "Roboto", Arial, sans-serif;
  }
  .bowl-shadow {
    position: absolute;
    left: -220px; top: 130px;
    width: 780px; height: 780px;
    border-radius: 50%;
    background: radial-gradient(circle, rgba(0,0,0,0.10) 0%, rgba(0,0,0,0.04) 50%, rgba(255,255,255,0) 70%);
  }
  .salad-photo {
    position: absolute;
    left: -120px; top: 175px;
    width: 585px; height: 585px;
    border-radius: 50%;
    background:
      radial-gradient(circle at 48% 52%, #4c8a33 0%, #5f9d3d 28%, #b8505a 48%, #7f9f52 58%, #ece6e4 70%, #f6f3f4 84%, #ffffff 100%);
  }
  .brand {
    position: absolute;
    left: 66px; top: 80px;
    display: flex; align-items: center; gap: 14px;
  }
  .brand-mark {
    width: 56px; height: 56px;
    background: var(--blue);
  }
  .brand-name {
    font-family: "Open Sans", Arial, sans-serif;
    font-weight: 400;
    font-size: 31px;
    color: var(--grey);
    letter-spacing: -0.5px;
  }
  .booth-ribbon {
    position: absolute;
    left: 987px; top: 0;
    width: 138px; height: 156px;
    background: var(--blue);
    clip-path: polygon(0 0, 100% 0, 100% 100%, 50% 88%, 0 100%);
    color: var(--white);
    text-align: center;
    padding-top: 46px;
  }
  .booth-label { font-size: 33px; font-weight: 300; line-height: 1; }
  .booth-number { font-size: 52px; font-weight: 700; line-height: 0.95; }
  .headline {
    position: absolute;
    left: 473px; top: 78px;
    color: var(--green);
    font-weight: 400;
    font-size: 76px;
    line-height: 82px;
    letter-spacing: -0.5px;
  }
  .stats {
    position: absolute;
    left: 457px; top: 350px;
    width: 700px;
    display: flex;
    justify-content: space-between;
  }
  .stat { width: 230px; text-align: center; }
  .stat-icon { height: 96px; display: flex; align-items: center; justify-content: center; }
  .stat-text {
    margin-top: 14px;
    font-family: "Work Sans", Arial, sans-serif;
    font-size: 17px;
    line-height: 22px;
    letter-spacing: 0.4px;
    color: var(--ink);
  }
  .stat-text b { font-weight: 600; }
  .map-area {
    width: 152px; height: 92px;
    background: var(--green);
    border-radius: 30px 18px 40px 26px;
    display: flex; align-items: center; justify-content: center;
    color: var(--white);
    font-weight: 700;
    font-size: 21px;
  }
  .service-band {
    position: absolute;
    left: 0; top: 560px;
    width: 1200px; height: 140px;
    background: var(--blue);
    color: var(--white);
  }
  .free-title {
    position: absolute;
    left: 66px; top: 24px;
    line-height: 1;
  }
  .free-title .free { display: block; font-size: 40px; font-weight: 700; }
  .free-title .service { display: block; font-size: 52px; font-weight: 300; margin-top: 2px; }
  .service-divider {
    position: absolute;
    top: 46px;
    width: 2px; height: 52px;
    background: var(--white);
  }
  .service-item {
    position: absolute;
    font-size: 24px;
    line-height: 33px;
    font-weight: 400;
  }
  .contact-line {
    position: absolute;
    left: 308px; top: 722px;
    width: 830px;
    display: flex;
    justify-content: space-between;
    align-items: center;
    font-family: "Open Sans", Arial, sans-serif;
    font-weight: 600;
    font-size: 18px;
    color: var(--blue-text);
  }
  .contact-dot { width: 8px; height: 8px; border-radius: 50%; background: var(--blue-text); }
</style>
</head>
<body>
<main class="ad">
  <div class="bowl-shadow"></div>
  <div class="salad-photo" role="img" aria-label="Photo of a spinach salad with strawberries, walnuts and feta in a white bowl"></div>

  <div class="brand">
    <span class="brand-mark"></span>
    <span class="brand-name">Pantry Hub Direct</span>
  </div>

  <div class="booth-ribbon">
    <div class="booth-label">Booth</div>
    <div class="booth-number">505</div>
  </div>

  <h1 class="headline">WE MAKE<br>FOOD &amp; SUPPLY<br>PURCHASING EASY</h1>

  <section class="stats">
    <div class="stat">
      <div class="stat-icon">
        <svg width="100" height="84" viewBox="0 0 100 84" aria-hidden="true">
          <polygon points="14,2 86,2 100,28 0,28" fill="var(--green)"/>
          <polygon points="22,7 78,7 88,24 12,24" fill="var(--paper)"/>
          <circle cx="50" cy="14" r="11" fill="var(--green)"/>
          <text x="50" y="19" text-anchor="middle" font-family="Roboto, sans-serif" font-weight="700" font-size="14" fill="var(--paper)">$</text>
          <g fill="var(--green)">
            <rect x="0" y="30" width="100" height="3"/><rect x="0" y="36" width="100" height="3"/>
            <rect x="0" y="42" width="100" height="3"/><rect x="0" y="48" width="100" height="3"/>
            <rect x="0" y="54" width="100" height="3"/><rect x="0" y="60" width="100" height="3"/>
            <rect x="0" y="66" width="100" height="3"/><rect x="0" y="72" width="100" height="3"/>
            <rect x="0" y="78" width="100" height="3"/>
          </g>
        </svg>
      </div>
      <p class="stat-text"><b>Since 1999</b>, we’ve<br>saved organizations<br>over <b>$100,000,000</b></p>
    </div>
    <div class="stat">
      <div class="stat-icon">
        <div class="map-area" role="img" aria-label="Map of the United States">6,000+</div>
      </div>
      <p class="stat-text">We serve <b>6,000+</b><br>organizations<br>across <b>46 states</b></p>
    </div>
    <div class="stat">
      <div class="stat-icon">
        <svg width="132" height="92" viewBox="0 0 132 92" aria-hidden="true">
          <polygon points="30,3 56,32 46,32 46,88 14,88 14,32 4,32" fill="none" stroke="var(--green-pale)" stroke-width="5" stroke-linejoin="round"/>
          <polygon points="84,3 114,3 114,56 126,56 100,88 72,56 84,56" fill="none" stroke="var(--green-pale)" stroke-width="5" stroke-linejoin="round"/>
          <circle cx="66" cy="48" r="24" fill="var(--green)"/>
          <text x="66" y="61" text-anchor="middle" font-family="Roboto, sans-serif" font-weight="700" font-size="36" fill="var(--paper)">$</text>
        </svg>
      </div>
      <p class="stat-text">Estimated <b>saving</b><br>for our customers<br>are <b>10-35%</b></p>
    </div>
  </section>

  <section class="service-band">
    <h2 class="free-title"><span class="free">100% FREE</span><span class="service">SERVICE</span></h2>
    <span class="service-divider" style="left:339px"></span>
    <p class="service-item" style="left:380px; top:22px">Food Purchases<br>Menu Planning<br>Recipes</p>
    <span class="service-divider" style="left:598px"></span>
    <p class="service-item" style="left:639px; top:38px">Use of Registered<br>Dietitian</p>
    <span class="service-divider" style="left:874px"></span>
    <p class="service-item" style="left:915px; top:38px">Discounted PPE and<br>Necessary Supplies</p>
  </section>

  <footer class="contact-line">
    <span>www.pantryhubdirect-example.com</span>
    <span class="contact-dot"></span>
    <span>info@pantryhubdirect-example.com</span>
    <span class="contact-dot"></span>
    <span>555.010.4520</span>
  </footer>
</main>
</body>
</html>
```